Tovrani business needs logo and business card designed

I need designed business card. it needs to have some wow effect, but simple, corporate and business focused. We provide corporate grade IT services to medium size businesses. These services are IT support over phone, email, in person, VOIP services, IT security , networking - everything that helps business be productivy.

Out tag line will be something along these lines" promoting business growth through use of technology:.

I need a logo designed as well. I am happy to use any colors/theme, perhaps neutral colours, earthy?

Priority: NICE looking, wow design, nice fonts, colors etc... nice logo, business focused but HAS to be modern, wow effect. I will accept anything that looks really cool.

Target Market(s)

Target market are businesses with 20-100 employees. Audience are business decision makers, like general managers, CEO, directors, those are the one seeing this business card;

Industry/Entity Type

Business

Contact Information for Business Card

I am totally flexible, suprise me me something creative:

Dorian Velmek logo on this side(you will design)
managing director ------------------------------- this is line
slogan: technology.delivered.simple

Level 3, 48 Pemberwick Street, Sydney, NSW 2000
dorian@tovrani.com.au
www.tovrani.com.au

back page: logo and slogan: promoting business growth through use of technolog

Requirements
Must have
• Must look modern, cool., wow effect, yet simple and professional.

```html
<!DOCTYPE html>
<html lang="en">
<head>
<meta charset="utf-8">
<title>Tovrani Business Card</title>
<link rel="stylesheet" href="https://fonts.googleapis.com/css2?family=PT+Sans:wght@700&family=Questrial&display=swap">
<style>
  :root {
    --teal: #4ea79f;
    --charcoal: #262626;
    --charcoal-light: #2f2f2f;
    --white: #ffffff;
    --address-blue: #5a9fc4;
    --page: #ffffff;
  }
  * { margin: 0; padding: 0; box-sizing: border-box; }
  html, body {
    width: 1200px;
    height: 2741px;
    overflow: hidden;
    background: var(--page);
  }
  .canvas { position: relative; width: 1200px; height: 2741px; }

  .card {
    position: absolute;
    left: 165px;
    overflow: hidden;
    background: var(--charcoal);
  }
  .card--back  { top: 204px;  width: 816px; height: 1092px; }
  .card--front { top: 1401px; width: 831px; height: 1113px; }

  .card__texture {
    position: absolute;
    inset: 0;
    background: radial-gradient(ellipse at 50% 40%, var(--charcoal-light), var(--charcoal) 75%);
  }

  .band {
    position: absolute;
    left: 0;
    right: 0;
    background: var(--teal);
  }

  .brand {
    position: absolute;
    left: 0;
    right: 0;
    display: flex;
    align-items: center;
    justify-content: center;
    gap: 26px;
    font-family: "PT Sans", "Helvetica Neue", sans-serif;
    font-weight: 700;
    color: var(--white);
    letter-spacing: -1px;
  }
  .brand__dot {
    width: 44px;
    height: 44px;
    border-radius: 50%;
    background: var(--charcoal);
    flex: none;
  }

  .card--back .band--head { top: 255px; height: 237px; }
  .card--back .brand { top: 255px; height: 237px; font-size: 96px; }

  .tagline {
    position: absolute;
    left: 0; right: 0; bottom: 0;
    height: 82px;
    background: var(--teal);
    display: flex;
    align-items: center;
    justify-content: center;
    font-family: "PT Sans", "Helvetica Neue", sans-serif;
    font-weight: 700;
    font-size: 30px;
    color: var(--white);
  }

  .card--front .band--head { top: 0; height: 402px; }
  .card--front .brand {
    top: 0;
    height: 402px;
    flex-direction: column;
    gap: 40px;
    font-size: 96px;
    padding-top: 40px;
  }
  .card--front .brand__dot { width: 110px; height: 110px; }

  .contact {
    position: absolute;
    left: 39px;
    top: 690px;
    font-family: "Questrial", "Century Gothic", sans-serif;
    color: var(--white);
  }
  .contact__name { position: absolute; top: -165px; left: 0; font-size: 68px; white-space: nowrap; letter-spacing: 1px; }
  .contact__role { position: absolute; top: -90px; left: 0; font-size: 36px; color: var(--teal); white-space: nowrap; letter-spacing: 1px; }
  .contact__row { position: absolute; left: 0; display: flex; align-items: baseline; white-space: nowrap; }
  .contact__label { width: 111px; font-size: 39px; color: var(--teal); }
  .contact__value { font-size: 24px; }
  .contact__row--web  { top: 0; }
  .contact__row--mail { top: 54px; }
  .contact__address { position: absolute; top: 125px; left: 0; font-size: 24px; line-height: 45px; white-space: nowrap; }
  .contact__address span { display: block; }
  .contact__address .contact__city { color: var(--address-blue); padding-left: 36px; }
</style>
</head>
<body>
<div class="canvas">

  <section class="card card--back">
    <div class="card__texture" role="img" aria-label="Dark charcoal mosaic texture"></div>
    <div class="band band--head"></div>
    <div class="brand"><span class="brand__dot"></span><span class="brand__name">Tovrani</span></div>
    <div class="tagline">Systems.Made.Effortless</div>
  </section>

  <section class="card card--front">
    <div class="card__texture" role="img" aria-label="Dark charcoal mosaic texture"></div>
    <div class="band band--head"></div>
    <div class="brand"><span class="brand__dot"></span><span class="brand__name">Tovrani</span></div>

    <div class="contact">
      <div class="contact__name">Dorian Velmek</div>
      <div class="contact__role">Managing Director</div>
      <div class="contact__row contact__row--web"><span class="contact__label">Web</span><span class="contact__value">www.tovrani.com.au</span></div>
      <div class="contact__row contact__row--mail"><span class="contact__label">Mail</span><span class="contact__value">dorian@tovrani.com.au</span></div>
      <div class="contact__address">
        <span>Level 3, 48 Pemberwick Street,</span>
        <span class="contact__city">Sydney, NSW 2000</span>
      </div>
    </div>

    <div class="tagline">Systems.Made.Effortless</div>
  </section>

</div>
</body>
</html>
```